Bref créative
Torvane
A GroomHaven for Men
Modern
Torvane - A GroomHaven for Men
The Lanterns
Mill Crescent
Ware
KT34 7RW
team@torvane.example
www.torvane.example
Name of Barbers is Torvane
Tag is - A GroomHaven for Men which must feature as part of logo.
GroomHaven is as spelt here (one word - capital B and S)
Use a derivative of the logo
These are the logo eps files. There is also a jpeg file uploaded so you can see the version I require for the design
this is logo version to use but use the eps file version for actual design

```html
<!DOCTYPE html>
<html lang="en">
<head>
<meta charset="utf-8">
<title>Torvane – Stationery Set</title>
<link href="https://fonts.googleapis.com/css2?family=Montserrat:wght@400;600&display=swap" rel="stylesheet">
<style>
  :root {
    --backdrop: #e9e4df;
    --paper: #ffffff;
    --band-dark: #2f3033;
    --band-light: #6b6d72;
    --ink: #3a3b3e;
    --ink-soft: #8a8c90;
    --ink-on-dark: #c9cacd;
    --edge: #d6d6d6;
    --shadow: rgba(0,0,0,0.18);
  }
  * { box-sizing: border-box; margin: 0; padding: 0; }
  html, body { width: 1200px; height: 482px; overflow: hidden; }
  body {
    background: var(--backdrop);
    font-family: "Montserrat", sans-serif;
    color: var(--ink);
    position: relative;
  }
  .sheet {
    position: absolute;
    background: var(--paper);
    border: 1px solid var(--edge);
    box-shadow: 2px 3px 6px var(--shadow);
    overflow: hidden;
  }
  .band {
    position: absolute; left: 0; right: 0; top: 0;
    background: linear-gradient(180deg, var(--band-dark), var(--band-light));
  }
  .wordmark { position: absolute; line-height: 1; white-space: nowrap; }
  .wordmark .name { font-weight: 600; letter-spacing: 0.16em; display: block; }
  .wordmark .tag { font-weight: 400; letter-spacing: 0.04em; display: block; margin-top: 2px; color: var(--ink-soft); }
  .wordmark.on-dark .name { color: #ffffff; }
  .wordmark.on-dark .tag { color: var(--ink-on-dark); }
  .contact { position: absolute; font-size: 4.5px; line-height: 1.45; color: var(--ink-soft); white-space: nowrap; }

  /* business cards */
  .card { width: 113px; height: 64px; }
  .card .name { font-size: 7px; }
  .card .tag { font-size: 3.6px; }
  .card .wordmark { left: 8px; top: 9px; }
  .card .contact { left: 8px; bottom: 7px; font-size: 3.8px; }
  .card-front { left: 19px; top: 149px; }
  .card-back { left: 19px; top: 222px; }
  .card-back .band { height: 100%; }
  .card-back .contact { color: var(--ink-on-dark); }

  /* letterhead */
  .letterhead { left: 163px; top: 43px; width: 307px; height: 430px; }
  .letterhead .wordmark { left: 22px; top: 22px; }
  .letterhead .name { font-size: 10px; }
  .letterhead .tag { font-size: 4.5px; }
  .letterhead .footer { position: absolute; left: 0; right: 0; bottom: 10px; text-align: center; font-size: 4.5px; color: var(--ink-soft); white-space: nowrap; }

  /* envelopes */
  .env-top { left: 504px; top: 43px; width: 312px; height: 144px; }
  .env-top .band { height: 36px; }
  .env-top .wordmark { left: 0; right: 0; top: 9px; text-align: center; }
  .env-top .name { font-size: 10px; }
  .env-top .tag { font-size: 4px; }

  .env-mid { left: 504px; top: 202px; width: 312px; height: 189px; }
  .env-mid .band { height: 24px; }
  .env-mid .wordmark { right: 18px; top: 30px; text-align: right; }
  .env-mid .name { font-size: 10px; }
  .env-mid .tag { font-size: 4px; }
  .env-mid .contact { left: 14px; bottom: 14px; }

  .env-right { left: 854px; top: 192px; width: 332px; height: 197px; }
  .env-right .flap { position: absolute; left: 0; top: 0; width: 100%; height: 46px; }
  .env-right .wordmark.main { left: 14px; top: 60px; }
  .env-right .wordmark.main .name { font-size: 11px; }
  .env-right .wordmark.main .tag { font-size: 4.5px; }
  .env-right .wordmark.return { right: 70px; top: 18px; text-align: right; }
  .env-right .wordmark.return .name { font-size: 9px; }
  .env-right .wordmark.return .tag { font-size: 4px; }
</style>
</head>
<body>

  <section class="sheet card card-front" aria-label="Business card front">
    <div class="wordmark"><span class="name">TORVANE</span><span class="tag">A GroomHaven for Men</span></div>
    <div class="contact">team@torvane.example<br>www.torvane.example</div>
  </section>

  <section class="sheet card card-back" aria-label="Business card back">
    <div class="band"></div>
    <div class="wordmark on-dark"><span class="name">TORVANE</span><span class="tag">A GroomHaven for Men</span></div>
    <div class="contact">The Lanterns, Mill Crescent<br>Ware KT34 7RW</div>
  </section>

  <section class="sheet letterhead" aria-label="Letterhead">
    <div class="wordmark"><span class="name">TORVANE</span><span class="tag">A GroomHaven for Men</span></div>
    <p class="footer">The Lanterns, Mill Crescent, Ware, KT34 7RW &nbsp;|&nbsp; team@torvane.example &nbsp;|&nbsp; www.torvane.example</p>
  </section>

  <section class="sheet env-top" aria-label="Envelope back">
    <div class="band"></div>
    <div class="wordmark on-dark"><span class="name">TORVANE</span><span class="tag">A GroomHaven for Men</span></div>
  </section>

  <section class="sheet env-mid" aria-label="Envelope front">
    <div class="band"></div>
    <div class="wordmark"><span class="name">TORVANE</span><span class="tag">A GroomHaven for Men</span></div>
    <div class="contact">The Lanterns<br>Mill Crescent, Ware<br>KT34 7RW</div>
  </section>

  <section class="sheet env-right" aria-label="Envelope with flap">
    <svg class="flap" viewBox="0 0 332 46" preserveAspectRatio="none" aria-hidden="true">
      <polyline points="0,0 12,44 320,44 332,0" fill="none" stroke="#dcdcdc" stroke-width="1"/>
    </svg>
    <div class="wordmark return"><span class="name">TORVANE</span><span class="tag">A GroomHaven for Men</span></div>
    <div class="wordmark main"><span class="name">TORVANE</span><span class="tag">A GroomHaven for Men</span></div>
  </section>

</body>
</html>
```